Need Amazing Website for Consulting Company

We need an amazing website design for a Human Resources Consulting Company. This will be geared towards a more professional crowd, but we don't want it to be overly corporate and stuffy: Just, clean and professional and amazing. Please use the video link below for further instruction.

http://clipvesta.net/v/kqPzRmN4

Thank You.

PS Logo file has been attached.

Target Market(s)

The target marketing is small business owners who have employees. These owners cant afford an in-house HR person so they would hire this client to consult and do the work for them.

Industry/Entity Type

It Company

Font styles to use
Sans Serif

Requirements
Must have
• Please watch video:

Must have spot for video on homepage.
Nice to have
• Clean, professional, but not overly corporate, we want a personal and fun feel to this site a bit to separate them from all the other executive type sites. This site should have some LIFE to it and reflect a local brand that is doing great things.
Should not have
• Should not be just a corporate site, should not be overly stuffy, should not be overly boring.

```html
<!DOCTYPE html>
<html lang="en">
<head>
<meta charset="utf-8">
<title>Mesa Ridge HR Advisors</title>
<link rel="stylesheet" href="https://fonts.googleapis.com/css2?family=Open+Sans:wght@400;600;700&family=Roboto+Condensed:wght@400;700&family=Nunito:wght@700&display=swap">
<style>
:root{
  --red:#c0192e;
  --red-dark:#9e1022;
  --red-light:#d52a3e;
  --ink:#222;
  --grey:#8a8a8a;
  --line:#e4e4e4;
  --hero-dark:#141414;
  --white:#fff;
}
*{margin:0;padding:0;box-sizing:border-box}
html,body{width:1200px;height:1124px;overflow:hidden;background:var(--white);font-family:"Open Sans",Arial,sans-serif;color:var(--ink)}
.page{position:relative;width:1200px;height:1124px}

/* header */
.brand{position:absolute;left:150px;top:44px;display:flex;align-items:center;gap:12px}
.brand-mark{width:34px;height:34px;background:var(--red)}
.brand-name{font-family:"Open Sans",Arial,sans-serif;font-weight:700;font-size:26px;color:var(--ink);line-height:1.1;width:220px}
.contact{position:absolute;left:839px;top:50px;display:flex;gap:12px;align-items:center}
.contact-icon{width:45px;height:45px}
.contact-label{font-size:17px;color:#666;line-height:1.1}
.contact-phone{font-family:"Roboto Condensed",Arial,sans-serif;font-weight:700;font-size:25px;color:var(--red);letter-spacing:.5px}

/* navigation */
.nav{position:absolute;left:0;top:140px;width:1200px;height:46px;background:linear-gradient(#d2283b,#b3172a);display:flex;padding-left:150px}
.nav a{display:flex;align-items:center;justify-content:center;height:46px;color:var(--white);text-decoration:none;font-family:"Roboto Condensed",Arial,sans-serif;font-size:18px;text-transform:uppercase;border-right:1px solid rgba(0,0,0,.18);box-shadow:inset -1px 0 0 rgba(255,255,255,.12)}
.nav a.current{background:linear-gradient(#2a2a2a,#111)}

/* hero */
.hero{position:absolute;left:0;top:186px;width:1200px;height:310px;background:radial-gradient(ellipse at 62% 40%,#3a3a3a 0%,#1f1f1f 45%,var(--hero-dark) 100%)}
.hero-fade{position:absolute;left:0;top:496px;width:1200px;height:110px;background:linear-gradient(#d6d6d6,#fff)}
.video{position:absolute;left:150px;top:242px;width:460px;height:314px;background:var(--white);padding:8px;box-shadow:0 8px 10px -6px rgba(0,0,0,.35)}
.video-screen{position:relative;width:100%;height:100%;background:radial-gradient(ellipse at center,#fff 30%,#bcbcbc 100%);text-align:center}
.video-title{position:absolute;left:0;right:0;top:90px;font-weight:700;font-size:30px;color:#111}
.video-text{position:absolute;left:16px;right:16px;top:224px;font-size:7.5px;line-height:1.6;color:#222}
.video-sign{position:absolute;left:0;right:0;top:262px;font-size:7.5px}
.video-play{position:absolute;left:192px;top:132px;width:52px;height:52px}
.hero-title{position:absolute;left:669px;top:258px;font-family:"Nunito",Arial,sans-serif;font-weight:700;font-size:34px;color:var(--white);letter-spacing:.5px}
.hero-text{position:absolute;left:670px;top:306px;width:390px;font-size:15px;line-height:23.5px;color:#eee}
.hero-button{position:absolute;left:670px;top:392px;width:207px;height:44px;background:var(--red);border:2px solid var(--red-dark);display:flex;align-items:center;justify-content:center;color:var(--white);font-weight:700;font-size:17px;box-shadow:0 2px 3px rgba(0,0,0,.4)}
.dots{position:absolute;left:670px;top:534px;display:flex;gap:7px}
.dots span{width:12px;height:12px;border-radius:50%;background:#d0d0d0;box-shadow:inset 0 1px 2px rgba(0,0,0,.3)}
.dots span.active{background:var(--red)}

/* services */
.section-head{position:absolute;left:0;top:626px;width:1200px;display:flex;justify-content:center;align-items:center;gap:12px}
.section-rule{width:144px;height:1px;background:var(--line)}
.section-title{font-size:21px;font-weight:600;color:#333;text-transform:uppercase}
.arrow{width:0;height:0;border-top:5px solid transparent;border-bottom:5px solid transparent}
.arrow.right{border-left:7px solid #ccc}
.arrow.left{border-right:7px solid #ccc}
.section-sub{position:absolute;left:0;top:661px;width:1200px;text-align:center;font-size:16.5px;color:var(--grey)}
.cards{position:absolute;left:150px;top:721px;display:flex;gap:24px}
.card{position:relative;width:284px;height:302px;border:1px solid var(--line);box-shadow:0 1px 2px rgba(0,0,0,.05);text-align:center}
.card-photo{height:185px;background:linear-gradient(135deg,#e9eef2,#c9c4bf)}
.card-photo.office{background:linear-gradient(135deg,#f2f2f2,#cfd2d6 60%,#9aa0a7)}
.card-photo.meeting{background:linear-gradient(135deg,#f5f1ec,#d9cbbd 60%,#b59c86)}
.card-plus{position:absolute;left:124px;top:167px;width:36px;height:36px}
.card-title{margin-top:34px;font-weight:700;font-size:16.5px;color:#222;text-transform:uppercase}
.card-text{margin-top:8px;font-size:14.5px;line-height:20px;color:var(--grey)}

/* footer */
.footer{position:absolute;left:0;top:1076px;width:1200px;height:48px;background:var(--red)}
.copyright{position:absolute;left:150px;top:16px;font-size:12.5px;color:#f3d6da}
.social{position:absolute;left:872px;top:11px;display:flex;gap:10px}
.social span{width:26px;height:26px;background:var(--red-dark);box-shadow:inset 0 1px 2px rgba(0,0,0,.3)}
</style>
</head>
<body>
<div class="page">
  <header>
    <div class="brand"><span class="brand-mark"></span><span class="brand-name">Mesa Ridge HR Advisors</span></div>
    <div class="contact">
      <svg class="contact-icon" viewBox="0 0 45 45" aria-hidden="true"><circle cx="22.5" cy="22.5" r="21" fill="none" stroke="#555" stroke-width="2"/><path d="M16 13c1.5-1 2.5-.6 3.3.6l1.8 3c.6 1 .3 2-.6 2.6l-1.4.9c.9 2.4 3.3 5 5.8 6.1l.9-1.4c.6-.9 1.6-1.2 2.6-.6l3 1.8c1.2.8 1.6 1.8.6 3.3-1.5 2.3-3.6 2.9-6.2 1.8-4.8-2-8.5-5.8-10.4-10.5-1-2.6-.5-4.6 1.6-6.1z" fill="#555"/></svg>
      <div><div class="contact-label">Questions? Call us at</div><div class="contact-phone">(123) - 234 - 5678</div></div>
    </div>
  </header>

  <nav class="nav">
    <a class="current" style="width:94px">Home</a>
    <a style="width:122px">About Us</a>
    <a style="width:121px">Services</a>
    <a style="width:120px">Staffing</a>
    <a style="width:121px">Partners</a>
    <a style="width:132px">Our Team</a>
    <a style="width:136px">Contact Us</a>
  </nav>

  <section class="hero"></section>
  <div class="hero-fade"></div>
  <div class="video">
    <div class="video-screen" role="img" aria-label="Introductory company video">
      <div class="video-title">Mesa Ridge HR Advisors</div>
      <svg class="video-play" viewBox="0 0 52 52" aria-hidden="true"><circle cx="26" cy="26" r="24" fill="rgba(255,255,255,.45)" stroke="#fff" stroke-width="2.5"/><path d="M20 15l17 11-17 11z" fill="#fff"/></svg>
      <p class="video-text">Mesa Ridge HR Advisors, LLC. (MRHA) is an <b><i>experienced</i></b> advisory agency that is committed to providing businesses with <b><i>effective</i></b> and <b><i>efficient</i></b> Human Resources support by building partnerships to meet each company's needs.</p>
      <p class="video-sign">MRHA, LLC.</p>
    </div>
  </div>
  <h1 class="hero-title">Consectetur Vestibulum</h1>
  <p class="hero-text">Lorem Ipsum is simply dummy text of the printing and typesetting industry. Lorem Ipsum has been the industry's standard dummy text ever since the.</p>
  <div class="hero-button">MORE INFORMATION</div>
  <div class="dots"><span></span><span class="active"></span><span></span><span></span></div>

  <div class="section-head"><span class="section-rule"></span><span class="arrow right"></span><h2 class="section-title">Mesa Ridge Services</h2><span class="arrow left"></span><span class="section-rule"></span></div>
  <p class="section-sub">Dolor sit amet, consectetur adipiscing Vestibulum ultrices tellus mi</p>

  <div class="cards">
    <article class="card">
      <div class="card-photo office" role="img" aria-label="Photo of a consultant working at a laptop in a bright office"></div>
      <svg class="card-plus" viewBox="0 0 36 36" aria-hidden="true"><circle cx="18" cy="18" r="17" fill="#c0192e" stroke="#fff" stroke-width="2"/><path d="M18 11v14M11 18h14" stroke="#fff" stroke-width="3"/></svg>
      <h3 class="card-title">Lorem Ipsum Dolor</h3>
      <p class="card-text">Dolor sit amet, consectetur adipiscing<br>Vestibulum ultrices tellus mi</p>
    </article>
    <article class="card">
      <div class="card-photo" role="img" aria-label="Photo of two colleagues reviewing documents together"></div>
      <svg class="card-plus" viewBox="0 0 36 36" aria-hidden="true"><circle cx="18" cy="18" r="17" fill="#c0192e" stroke="#fff" stroke-width="2"/><path d="M18 11v14M11 18h14" stroke="#fff" stroke-width="3"/></svg>
      <h3 class="card-title">Lorem Ipsum Dolor</h3>
      <p class="card-text">Dolor sit amet, consectetur adipiscing<br>Vestibulum ultrices tellus mi</p>
    </article>
    <article class="card">
      <div class="card-photo meeting" role="img" aria-label="Photo of a small team meeting around a table"></div>
      <svg class="card-plus" viewBox="0 0 36 36" aria-hidden="true"><circle cx="18" cy="18" r="17" fill="#c0192e" stroke="#fff" stroke-width="2"/><path d="M18 11v14M11 18h14" stroke="#fff" stroke-width="3"/></svg>
      <h3 class="card-title">Lorem Ipsum Dolor</h3>
      <p class="card-text">Dolor sit amet, consectetur adipiscing<br>Vestibulum ultrices tellus mi</p>
    </article>
  </div>

  <footer class="footer">
    <p class="copyright">Copyright © 2014 Mesa Ridge Advisors. All Rights Reserved.</p>
    <div class="social" aria-label="Social links"><span></span><span></span><span></span><span></span><span></span></div>
  </footer>
</div>
</body>
</html>
```